The project is a book cover for a health/recipe book for both Kindle and a future soft cover. Title is Morning Garden Table: Gather Greens and Steady Your Days with a subtitle Six Weeks of Gentle Kitchen Habits. I am a registed dietitian nutritionist specializing in midlife and senior women to help them look and feel 10 years younger by balancing hormones and curbing inflammationI like the idea of fresh colorful whole foods on the cover with a natural clean look. But I am also open to a cover which expresses vitality--perhaps a woman or couple whose "being" expresses energy and vitality.Since I am unsure right at this moment the exact # of pages for the book, I will need to have some wiggle room in the final stages to get the spine dimensions.I am happy to send a table of contents if that would help.I need to decide on a cover in the next 2 weeks. Below are some ideas on style that I like with reservations. Background on 1 is too dark, 2 is too pastel and 3 is good but doesn't move me as much and my followers liked it the least
Updates
Entered wrong completion date and would like more entries.
Target Market(s)
Woman 40 to 65+, college educated
Industry/Entity Type
Nutrition
Colors
Designer to choose colors to be used in the design.
Look and feel
Each slider illustrates characteristics of the customer's brand and the style your logo design should communicate.

```html
<!DOCTYPE html>
<html lang="en">
<head>
<meta charset="utf-8">
<title>Morning Garden Table — Book Cover</title>
<link rel="stylesheet" href="https://fonts.googleapis.com/css2?family=Tinos:wght@400&family=Open+Sans:wght@700&display=swap">
<style>
  :root {
    --cream-top: #fbf7e6;
    --cream-mid: #efe6c7;
    --beige-deep: #d9c99c;
    --title-green: #1f7a3a;
    --band-green: #2b7d3b;
    --white: #ffffff;
    --produce-red: #b8321f;
    --produce-green: #5c8a2e;
    --basket-brown: #9a6a34;
  }
  html, body {
    margin: 0;
    padding: 0;
    overflow: hidden;
    background: #ffffff;
  }
  .cover {
    position: relative;
    width: 802px;
    height: 1200px;
    overflow: hidden;
    background: radial-gradient(ellipse at 50% 35%, var(--cream-top) 0%, var(--cream-mid) 55%, var(--beige-deep) 100%);
  }
  .produce-photo {
    position: absolute;
    left: 0;
    top: 500px;
    width: 802px;
    height: 615px;
    background:
      linear-gradient(to bottom, rgba(239,230,199,1) 0%, rgba(239,230,199,0) 22%),
      radial-gradient(ellipse at 55% 45%, var(--basket-brown) 0%, rgba(154,106,52,0) 38%),
      radial-gradient(ellipse at 20% 80%, var(--produce-red) 0%, rgba(184,50,31,0) 35%),
      radial-gradient(ellipse at 85% 75%, var(--produce-red) 0%, rgba(184,50,31,0) 30%),
      radial-gradient(ellipse at 15% 55%, var(--produce-green) 0%, rgba(92,138,46,0) 30%),
      radial-gradient(ellipse at 88% 50%, var(--produce-green) 0%, rgba(92,138,46,0) 28%),
      linear-gradient(to bottom, #d8c79a 0%, #8f6b3c 100%);
  }
  .title {
    position: absolute;
    left: 0;
    width: 100%;
    margin: 0;
    text-align: center;
    font-family: "Tinos", "Times New Roman", serif;
    font-weight: 400;
    color: var(--title-green);
  }
  .title-main {
    top: 48px;
    font-size: 122px;
    line-height: 1;
    letter-spacing: 2px;
  }
  .title-second {
    top: 218px;
    font-size: 104px;
    line-height: 1;
  }
  .subtitle {
    position: absolute;
    top: 372px;
    left: 0;
    width: 100%;
    margin: 0;
    text-align: center;
    font-family: "Tinos", "Times New Roman", serif;
    font-size: 46px;
    line-height: 64px;
    color: var(--title-green);
  }
  .tagline {
    position: absolute;
    top: 980px;
    left: 0;
    width: 100%;
    margin: 0;
    text-align: center;
    font-family: "Open Sans", Arial, sans-serif;
    font-weight: 700;
    font-size: 40px;
    color: var(--white);
    text-shadow: 0 2px 8px rgba(0,0,0,0.55);
  }
  .author-band {
    position: absolute;
    left: 0;
    bottom: 0;
    width: 100%;
    height: 85px;
    background: var(--band-green);
    display: flex;
    align-items: center;
    justify-content: center;
  }
  .author-name {
    margin: 0;
    font-family: "Open Sans", Arial, sans-serif;
    font-weight: 700;
    font-size: 48px;
    letter-spacing: 2px;
    color: var(--white);
  }
</style>
</head>
<body>
  <main class="cover">
    <div class="produce-photo" role="img" aria-label="Wicker basket of fresh whole foods: bread, grapes, broccoli, red peppers, eggplant, cabbage, apples, bottles of olive oil, juice and wine"></div>

    <h1 class="title title-main">MORNING</h1>
    <p class="title title-second">Garden Table:</p>
    <p class="subtitle">Gather Greens and<br>Steady Your Days</p>

    <p class="tagline">Six Weeks of Gentle Kitchen Habits</p>

    <footer class="author-band">
      <p class="author-name">AUTHOR´S NAME</p>
    </footer>
  </main>
</body>
</html>
```